Business Card Design Project

i have the logo designed.
I require designs for the managing director and the general manager.
we need space for email, and a mobile number.
any other cool stuff/design you guys just let me see what you got.
The managing director card could be black, minimalist, and the cards for the rest of the company could be using the green logo.
it has to impress. transportation market is fragmented, we want to appear professional and sophisticated.
Md: Tarek bani rahim
General manager: omer rahim
clients: procurement heads of contracting companies
Business

```html
<!DOCTYPE html>
<html lang="en">
<head>
<meta charset="utf-8">
<title>Tralvexo — Managing Director Business Card</title>
<link rel="stylesheet" href="https://fonts.googleapis.com/css2?family=Open+Sans:wght@300;400;700&family=Quicksand:wght@300;400&display=swap">
<style>
  :root {
    --backdrop: #2a2a2a;
    --card: #111111;
    --card-band: #161616;
    --card-edge: #1c1c1c;
    --ink: #f2f2f2;
    --ink-soft: #c4c4c4;
    --ink-muted: #8f8f8f;
  }
  * { box-sizing: border-box; margin: 0; padding: 0; }
  html, body {
    width: 1200px; height: 900px; overflow: hidden;
    background: var(--backdrop);
    font-family: "Open Sans", Arial, sans-serif;
  }
  .sheet {
    width: 1200px; height: 900px;
    display: flex; flex-direction: column;
    align-items: center; justify-content: center; gap: 60px;
  }
  .card {
    position: relative;
    width: 560px; height: 320px;
    background: var(--card);
    border: 1px solid var(--card-edge);
    box-shadow: 0 18px 40px rgba(0,0,0,0.55);
    overflow: hidden;
  }
  .card--back {
    background: linear-gradient(180deg, var(--card-band) 0 14%, var(--card) 14% 100%);
  }

  /* Card back: identity and contact */
  .identity {
    position: absolute; left: 0; top: 150px;
    padding-left: 36px;
    border-left: 10px solid var(--ink);
  }
  .identity__name {
    font-weight: 700; font-size: 20px; letter-spacing: 0.5px;
    text-transform: uppercase; color: var(--ink-soft);
    line-height: 1.2;
  }
  .identity__role {
    font-weight: 300; font-size: 19px; color: var(--ink-muted);
    margin-top: 2px;
  }
  .contact {
    position: absolute; right: 40px; top: 42px;
    font-weight: 300; font-size: 14px; color: var(--ink-muted);
    list-style: none;
  }
  .contact__row { display: flex; align-items: flex-start; gap: 14px; margin-bottom: 8px; }
  .contact__icon { width: 18px; flex: none; margin-top: 2px; }
  .contact__lines { line-height: 1.35; }

  /* Card front: brand */
  .brand {
    position: absolute; left: 0; right: 0; top: 92px;
    display: flex; align-items: center; justify-content: center; gap: 18px;
  }
  .brand__dot { width: 22px; height: 22px; border-radius: 50%; background: var(--ink); }
  .brand__name {
    font-weight: 700; font-size: 58px; color: var(--ink); letter-spacing: 0.5px;
    line-height: 1;
  }
  .front__email {
    position: absolute; left: 0; right: 0; bottom: 48px;
    text-align: center;
    font-family: "Quicksand", "Open Sans", sans-serif;
    font-weight: 300; font-size: 22px; letter-spacing: 12px;
    color: var(--ink-muted);
  }
</style>
</head>
<body>
<main class="sheet">
  <section class="card card--back" aria-label="Card back">
    <ul class="contact">
      <li class="contact__row">
        <svg class="contact__icon" viewBox="0 0 18 14" aria-hidden="true">
          <rect x="0.5" y="0.5" width="17" height="13" fill="none" stroke="#8f8f8f"/>
          <path d="M0.5 0.5 L9 8 L17.5 0.5" fill="none" stroke="#8f8f8f"/>
        </svg>
        <span class="contact__lines">tarek@tralvexo.com</span>
      </li>
      <li class="contact__row">
        <svg class="contact__icon" viewBox="0 0 18 24" aria-hidden="true">
          <rect x="3" y="0.5" width="12" height="23" rx="2" fill="none" stroke="#8f8f8f" stroke-width="1.4"/>
          <line x1="7" y1="20" x2="11" y2="20" stroke="#8f8f8f" stroke-width="1.4"/>
        </svg>
        <span class="contact__lines">+484 5550 1234<br>+484 5550 7654</span>
      </li>
    </ul>
    <div class="identity">
      <p class="identity__name">Tarek bani rahim</p>
      <p class="identity__role">Managing Director</p>
    </div>
  </section>

  <section class="card card--front" aria-label="Card front">
    <div class="brand">
      <span class="brand__dot" aria-hidden="true"></span>
      <span class="brand__name">Tralvexo</span>
    </div>
    <p class="front__email">hello@tralvexo.au</p>
  </section>
</main>
</body>
</html>
```